Book cover for "Steady Broker" focused on scaling up an Insurance Agency

Front Cover:
We need book cover for our upcoming book with title "Steady Broker" . Subtitle of book is "The secrets behind building a multi-million dollar Insurance agency:Interviews, success stories and framework for success".
On top line it should say " Foreword by Mark Holloway".
Author name : "Ravindra Kulkarni"
This book will help insurance agents in scaling up their agency. It will also help someone looking to start a business or side hustle.

Back Cover:
It should contain content provided below and image of author attached.
"
Who should read this book?

Do you know that starting an Insurance Agency is probably one of the best business ideas?
Do you want to know how some startups created billion dollar plus insurance based companies in the last 5-10 years?
Do you want to know the secrets behind building a multi-million dollar Insurance agency?
Do you want to know how to scale up an Insurance Agency profitably?
Do you want to know how to cut through the noise in the market and differentiate your business?
How to leverage technology to rise above (be seen and heard) the myriad of agencies around you and compete with both local and online agencies?
How to build a team which carries your mindset to take care of clients and grow your business?
(above list should be bulleted)
If you are interested in learning about these topics then you are at the right place.

You can either spend years figuring out things yourself or read this book and get wisdom from successful agents and thought leaders at top insurance agencies."

Spine:
" Steady Broker by Ravindra Kulkarni"

Requirements:
One file should be only book cover.
Other file should contain :front cover, back cover and spine as one file.
It should follow standard for Norvel PBX, link provided below.
https://pbx.norvelbooks.example/en_US/help/topic/Q774210385

Target Market(s)

Insurance Agents
People looking to start a new business
Side Hustlers

Industry/Entity Type

Insurance Agency

Font styles to use
Serif

```html
<!DOCTYPE html>
<html lang="en">
<head>
<meta charset="utf-8">
<title>Steady Broker — Book Cover</title>
<link rel="stylesheet" href="https://fonts.googleapis.com/css2?family=Noto+Serif:wght@400;700&display=swap">
<style>
  :root {
    --cover-green: #6b8d6b;
    --title-white: #ffffff;
    --ink-dark: #1f2420;
    --wall-grey: #cfd0cc;
    --wall-shadow: #8f918c;
    --window-light: #f3efe6;
    --window-frame: #4a3f36;
    --table-wood: #a8794c;
    --table-deep: #6e4c2f;
    --jacket-grey: #5f5e5a;
    --shirt-white: #e7e3dc;
  }
  html, body {
    margin: 0;
    padding: 0;
    width: 850px;
    height: 1200px;
    overflow: hidden;
    background: var(--cover-green);
  }
  .cover {
    position: relative;
    width: 850px;
    height: 1200px;
    background: var(--cover-green);
    font-family: "Noto Serif", Georgia, serif;
    overflow: hidden;
  }
  .cover-title {
    position: absolute;
    top: 110px;
    left: 0;
    width: 100%;
    margin: 0;
    text-align: center;
    color: var(--title-white);
    font-size: 54px;
    line-height: 1.2;
    font-weight: 700;
    text-shadow: 0 1px 2px rgba(0,0,0,0.15);
  }
  .cover-author {
    position: absolute;
    top: 199px;
    left: 0;
    width: 100%;
    margin: 0;
    text-align: center;
    color: var(--title-white);
    font-size: 25px;
    line-height: 1.2;
    font-weight: 700;
  }
  .cover-photo {
    position: absolute;
    top: 264px;
    left: 61px;
    width: 728px;
    height: 683px;
    background:
      radial-gradient(ellipse 22% 20% at 56% 60%, rgba(231,227,220,0.9) 0%, rgba(231,227,220,0) 100%),
      radial-gradient(ellipse 12% 34% at 17% 36%, rgba(95,94,90,0.85) 0%, rgba(95,94,90,0) 100%),
      radial-gradient(ellipse 30% 36% at 76% 28%, var(--window-light) 0%, rgba(243,239,230,0.6) 55%, rgba(243,239,230,0) 100%),
      linear-gradient(180deg, rgba(168,121,76,0) 0%, rgba(168,121,76,0) 58%, var(--table-wood) 74%, var(--table-deep) 100%),
      linear-gradient(90deg, var(--wall-grey) 0%, var(--wall-shadow) 40%, var(--window-frame) 52%, #7a6b5d 100%);
  }
  .cover-foreword {
    position: absolute;
    top: 1118px;
    left: 0;
    width: 100%;
    margin: 0;
    text-align: center;
    color: var(--title-white);
    font-size: 18px;
    line-height: 1.4;
    font-weight: 700;
  }
  .cover-subtitle {
    position: absolute;
    top: 1145px;
    left: 0;
    width: 100%;
    margin: 0;
    text-align: center;
    color: var(--title-white);
    font-size: 17px;
    line-height: 25px;
    font-weight: 700;
    letter-spacing: -0.2px;
    white-space: nowrap;
  }
</style>
</head>
<body>
  <main class="cover">
    <h1 class="cover-title">Steady Broker</h1>
    <p class="cover-author">by Ravindra Kulkarni</p>
    <div class="cover-photo" role="img" aria-label="Photograph of an insurance team meeting: a presenter in a grey jacket stands at a whiteboard while colleagues sit around a wooden table with laptops and coffee beside a large bright window"></div>
    <p class="cover-foreword">Foreword by Mark Holloway</p>
    <p class="cover-subtitle">“The secrets behind building a multi-million dollar insurance agency:<br>Interviews, success stories and framework for success”.</p>
  </main>
</body>
</html>
```